TBV business card

For a business card with our logo

Contact Information for Business Card

Lucien MARVET
Founder & CEO
email : ceo@brightlanternstudio.com / www.brightlanternstudio.com /
instagram / facebook / WhatsApp
N°: +590 690 482 517

Colors

Designer to choose colors to be used in the design.

```html
<!DOCTYPE html>
<html lang="en">
<head>
<meta charset="utf-8">
<title>Bright Lantern Studio – Business Card</title>
<link href="https://fonts.googleapis.com/css2?family=PT+Sans:wght@400;700&display=swap" rel="stylesheet">
<style>
  :root {
    --canvas: #e6e7e9;
    --paper: #ffffff;
    --brand-blue: #1f5bb0;
    --brand-orange: #f37a24;
    --ink: #2b2b2b;
    --band-text: #ffffff;
  }
  * { box-sizing: border-box; margin: 0; padding: 0; }
  html, body { width: 1200px; height: 1200px; overflow: hidden; }
  body {
    background: var(--canvas);
    font-family: "PT Sans", Arial, sans-serif;
    position: relative;
  }
  .card {
    position: absolute;
    left: 160px;
    width: 880px;
    height: 503px;
    background: var(--paper);
    box-shadow: 0 6px 18px rgba(0,0,0,0.18);
    overflow: hidden;
  }
  .card--front { top: 70px; }
  .card--back { top: 627px; }

  .brand {
    display: flex;
    align-items: center;
    gap: 18px;
  }
  .brand__dot {
    width: 78px; height: 78px;
    border-radius: 50%;
    background: var(--brand-orange);
    flex: none;
  }
  .brand__name {
    color: var(--brand-blue);
    font-weight: 700;
    font-size: 40px;
    line-height: 1.02;
    letter-spacing: 1px;
    white-space: nowrap;
  }
  .card--front .brand {
    position: absolute;
    left: 50%; top: 185px;
    transform: translateX(-50%);
  }

  .contact-band {
    position: absolute;
    left: 0; right: 0; bottom: 0;
    height: 58px;
    background: var(--brand-blue);
    display: flex;
    align-items: center;
    justify-content: center;
    gap: 34px;
    color: var(--band-text);
    font-size: 17px;
    white-space: nowrap;
  }
  .contact-band__item { display: flex; align-items: center; gap: 9px; }
  .contact-band__mark {
    width: 16px; height: 16px;
    background: var(--brand-orange);
    border-radius: 3px;
    flex: none;
  }

  .card--back .brand {
    position: absolute;
    left: 60px; top: 205px;
  }
  .card--back .brand__name { font-size: 34px; }
  .divider {
    position: absolute;
    left: 455px; top: 130px;
    width: 3px; height: 240px;
    background: var(--brand-blue);
  }
  .person {
    position: absolute;
    left: 495px; top: 140px;
  }
  .person__name {
    color: var(--brand-orange);
    font-weight: 700;
    font-size: 36px;
    letter-spacing: 0.5px;
    white-space: nowrap;
  }
  .person__role {
    color: var(--ink);
    font-size: 22px;
  }
  .person__contacts {
    list-style: none;
    margin-top: 18px;
    color: var(--ink);
    font-size: 21px;
  }
  .person__contacts li {
    display: flex; align-items: center; gap: 12px;
    line-height: 1.55;
    white-space: nowrap;
  }
  .person__contacts svg { width: 18px; height: 18px; flex: none; }
</style>
</head>
<body>

<section class="card card--front" aria-label="Card front">
  <div class="brand">
    <span class="brand__dot"></span>
    <span class="brand__name">BRIGHT LANTERN<br>STUDIO</span>
  </div>
  <div class="contact-band">
    <span class="contact-band__item"><span class="contact-band__mark"></span>/brightlanternstudio.official</span>
    <span class="contact-band__item"><span class="contact-band__mark"></span>@brightlanternstudio</span>
    <span class="contact-band__item"><span class="contact-band__mark"></span>+590 690 482 517</span>
  </div>
</section>

<section class="card card--back" aria-label="Card back">
  <div class="brand">
    <span class="brand__dot"></span>
    <span class="brand__name">BRIGHT LANTERN<br>STUDIO</span>
  </div>
  <div class="divider"></div>
  <div class="person">
    <p class="person__name">LUCIEN MARVET</p>
    <p class="person__role">Founder</p>
    <ul class="person__contacts">
      <li>
        <svg viewBox="0 0 24 24" aria-hidden="true"><path fill="#1f5bb0" d="M6.6 10.8a15 15 0 0 0 6.6 6.6l2.2-2.2a1 1 0 0 1 1-.25 11.4 11.4 0 0 0 3.6.57 1 1 0 0 1 1 1V20a1 1 0 0 1-1 1A17 17 0 0 1 3 4a1 1 0 0 1 1-1h3.5a1 1 0 0 1 1 1c0 1.25.2 2.45.57 3.57a1 1 0 0 1-.25 1z"/></svg>
        +590 690 482 517
      </li>
      <li>
        <svg viewBox="0 0 24 24" aria-hidden="true"><rect x="2" y="5" width="20" height="14" rx="1" fill="#1f5bb0"/><path d="M3 6l9 7 9-7" fill="none" stroke="#fff" stroke-width="1.6"/></svg>
        ceo@brightlanternstudio.com
      </li>
      <li>
        <svg viewBox="0 0 24 24" aria-hidden="true"><g fill="none" stroke="#1f5bb0" stroke-width="1.8"><circle cx="12" cy="12" r="9"/><ellipse cx="12" cy="12" rx="4" ry="9"/><path d="M3 12h18"/></g></svg>
        www.brightlanternstudio.com
      </li>
    </ul>
  </div>
</section>

</body>
</html>
```